Trendy E Juice Product Labels Required

We are looking for design for an e Juice label line (the liquids used in electronic cigarettes). What we need is 5 product labels which eventually will be printed on 95mm x 40mm labels. Obviously the image will be created much larger than this but the aspect ratio should be scalable down to this size.

What each label must have is I would need is a background, a monster character, and space for a product name incorporated in to the design. The brand on this line is "Velvet Pebble". Whilst creatively, we are completely open to any concept, there is certain text which is necessary for incorporation in to each label. The attached file, "Example Label" shows these elements. NOTE: the attached file IS NOT a finished label.
Updates

Reason: Not received a design that we wish to proceed with.

Target Market(s)

25-35 year old vapers

Industry/Entity Type

Electronic

Requirements
Should not have
• Anything that may be construed as being targeted toward children.

```html
<!DOCTYPE html>
<html lang="en">
<head>
<meta charset="utf-8">
<title>Velvet Pebble – E-Liquid Label</title>
<link rel="stylesheet" href="https://fonts.googleapis.com/css2?family=Barlow:ital,wght@0,400;0,600;0,700;1,400&family=Barlow+Condensed:wght@400&display=swap">
<style>
  :root {
    --lime: #8dc63f;
    --lime-soft: #b9dc84;
    --ink: #000000;
    --paper: #ffffff;
    --forest: #0d3a1f;
  }
  * { box-sizing: border-box; margin: 0; padding: 0; }
  html, body { width: 1200px; height: 505px; overflow: hidden; background: var(--paper); }
  .label {
    position: relative; width: 1200px; height: 505px;
    background: var(--ink); color: var(--paper);
    font-family: "Barlow", Arial, sans-serif;
    overflow: hidden;
  }
  .band { position: absolute; left: 0; width: 100%; height: 37px; background: var(--lime); }
  .band--top { top: 0; }
  .band--bottom { bottom: 0; }
  .panel { position: absolute; left: 0; top: 0; }

  .legal { position: absolute; left: 56px; width: 250px; }
  .legal h2 { font-size: 25px; font-weight: 700; letter-spacing: .5px; line-height: 1; margin-bottom: 3px; }
  .legal p { font-size: 15.8px; line-height: 20.6px; }
  .legal--warning { top: 58px; }
  .legal--ingredients { top: 336px; width: 260px; }
  .legal--ingredients p { line-height: 20.4px; }

  .mascot {
    position: absolute; left: 542px; top: 62px; width: 76px; height: 76px;
    border-radius: 50% 50% 44% 44%;
    background: radial-gradient(circle at 50% 40%, var(--lime-soft), var(--lime));
  }
  .brand {
    position: absolute; left: 390px; width: 380px; top: 146px;
    text-align: center; color: var(--lime);
    font-weight: 700; font-size: 70px; line-height: 76px; letter-spacing: 1px;
  }
  .product-name {
    position: absolute; left: 436px; top: 333px; width: 276px; height: 44px;
    background: var(--lime); color: var(--ink);
    font-family: "Barlow Condensed", Arial, sans-serif; font-size: 33px;
    display: flex; align-items: center; justify-content: center;
  }
  .volume {
    position: absolute; left: 500px; width: 150px; top: 409px;
    text-align: center; color: var(--ink); font-size: 19px;
  }

  .contact { position: absolute; left: 844px; }
  .contact--find { top: 60px; font-style: italic; font-size: 16px; }
  .social { position: absolute; left: 837px; top: 88px; display: flex; gap: 32px; }
  .social span { width: 64px; height: 64px; border-radius: 50%; background: var(--lime); display: block; }
  .contact--web { top: 166px; font-weight: 700; font-size: 16px; line-height: 25px; }
  .contact--distributor { top: 271px; font-size: 16.5px; line-height: 21.5px; }
  .marks { position: absolute; left: 842px; top: 384px; }
</style>
</head>
<body>
<div class="label">
  <div class="band band--top"></div>
  <div class="band band--bottom"></div>

  <svg class="panel" width="1200" height="505" viewBox="0 0 1200 505" aria-hidden="true">
    <polygon points="398,37 765,37 813,468 345,468" fill="var(--paper)"/>
  </svg>

  <section class="legal legal--warning">
    <h2>WARNING</h2>
    <p>This product contains nicotine, a substance which is knows to cause birth defects. Do not swallow. Avoid contact with skin. Keep out of reach of children and pets. This product is intended for use by persons 18 and older. Pregnant women and those breast feeding should not use this product. May contain traces of nuts.</p>
  </section>
  <section class="legal legal--ingredients">
    <h2>INGREDIENTS</h2>
    <p>USP/EP Propelyn Glycol (XX%), USP/EP Vetetable Glycerin (XX%), USP/EP Nicotine, Natural and Artificial Flavorings.</p>
  </section>

  <div class="mascot" role="img" aria-label="Monster character illustration"></div>
  <div class="brand">VELVET<br>PEBBLE</div>
  <div class="product-name">Product Name</div>
  <div class="volume">30ml</div>

  <div class="contact contact--find">Find us at:</div>
  <div class="social" aria-label="Social channels"><span></span><span></span><span></span></div>
  <div class="contact contact--web">www.velvetpebble.com<br>@velvetpebble</div>
  <div class="contact contact--distributor">Distributed by:<br>Velvet Pebble<br>Address<br>Telephone</div>

  <svg class="marks" width="320" height="66" viewBox="0 0 320 66" aria-label="Recycling, caution, disposal and age 18+ marks">
    <circle cx="35" cy="33" r="30" fill="var(--paper)"/>
    <g transform="translate(110 33)">
      <path d="M0,-30 L32,28 L-32,28 Z" fill="var(--paper)" stroke="var(--paper)" stroke-width="6" stroke-linejoin="round"/>
      <rect x="-4" y="-14" width="8" height="26" rx="3" fill="var(--ink)"/>
      <circle cx="0" cy="20" r="4.5" fill="var(--ink)"/>
    </g>
    <rect x="163" y="5" width="56" height="56" fill="var(--paper)"/>
    <g transform="translate(272 33)">
      <circle r="28" fill="none" stroke="var(--paper)" stroke-width="5"/>
      <text x="0" y="11" text-anchor="middle" font-family="Barlow, Arial, sans-serif" font-weight="700" font-size="32" fill="var(--paper)">18</text>
      <line x1="-20" y1="-20" x2="20" y2="20" stroke="var(--paper)" stroke-width="5"/>
    </g>
  </svg>
</div>
</body>
</html>
```